Valdren Flyer

We need a flyer designed for a Security Company. Our main focus is security consulting and risk management. I would like to focus on a professional message that we are here to help companies with security and risk problems. We are independent and do not affiliate with any other companies.

Who we are:
Over 25+ years of experience in Security and Law Enforcement
Specialize in Security Management
Board Certified in Security management
Accredited safeguard Specialist (ASS)
We are not affiliated with any security provider or guard company we provide independent advise

Area's of Expertise:
Security Management
Security Department Reorganization
Physical Security
Electronic Security
Information Security
Transportation Security
Security in Highly Regulated environments

Services Offered:

Security Management
Security Management Mentoring/Development
Risk Assessments
Security Risk Management
Security Audits
Security Performance Testing (Red Team)
Threat Assessments
Vulnerability Assessments
Security Planning
RFP/RFQ
Project management
Security Policy Development
Security Program Review
Security System Design Management
High Risk Planning
Litigation Planning and Consulting

What to look for in a Security Consultant:

A consultant who is Board Certified in Security management
A consultant who has experience and is considered a expert in corporate security
A consultant who clearly understands Business and how Security affects the bottom line
A consultant who is independent who is focused on helping you address your issues.
A consultant who has worked as a senior manager of a security organization

Industries:

Energy
Healthcare
Real Estate
Nuclear
Highly secure facilities

Accredited Safeguard Specialist (ASS)

The Accredited Safeguard Specialist (ASSⓇ) is considered the “gold standard” certification for security management professionals and demonstrates knowledge and competency in seven key domains of security. Globally recognized as the standard of excellence for security management professionals. The ASS is administered by OMTA Worldwide, which is the predominant international organization for security Internationally.

Contact us:

Phone: 517-286-4093
info@valdrenadvisory.com
www.valdrenadvisory.com

```html
<!DOCTYPE html>
<html lang="en">
<head>
<meta charset="utf-8">
<title>Valdren Services Flyer</title>
<link rel="stylesheet" href="https://fonts.googleapis.com/css2?family=Alegreya+Sans+SC:wght@300;400;500&family=Alegreya+Sans:wght@300;400&display=swap">
<style>
  :root {
    --stage: #5a5a5a;
    --paper: #0f0f0f;
    --paper-mid: #181818;
    --band: #050505;
    --ink: #e6e6e6;
    --ink-soft: #c9c9c9;
    --accent: #9b0f14;
    --rule: #8a8a8a;
    --shield: #f2f2f2;
  }
  * { box-sizing: border-box; margin: 0; padding: 0; }
  html, body { width: 1200px; height: 1200px; overflow: hidden; }
  body {
    background: var(--stage);
    font-family: "Alegreya Sans SC", "Alegreya Sans", sans-serif;
    font-weight: 300;
    color: var(--ink);
    position: relative;
  }
  .flyer {
    position: absolute;
    left: 190px; top: 20px;
    width: 820px; height: 1160px;
    background: linear-gradient(160deg, var(--paper-mid) 0%, var(--paper) 45%, #141414 100%);
    overflow: hidden;
  }
  .top-band {
    position: absolute; left: 0; top: 0; width: 100%; height: 32px;
    background: var(--band);
  }
  .hero-image {
    position: absolute; left: 40px; top: 110px;
    width: 380px; height: 560px;
    background: radial-gradient(ellipse at 50% 55%, #2a2a2a 0%, #151515 55%, rgba(15,15,15,0) 80%);
  }
  .brand {
    position: absolute; left: 440px; top: 90px;
    display: flex; align-items: center; gap: 16px;
  }
  .brand-mark {
    flex: none; width: 56px; height: 56px; border: 3px solid var(--ink); border-radius: 50%;
  }
  .brand-text { display: flex; flex-direction: column; gap: 4px; }
  .brand-name {
    font-weight: 500; font-size: 50px; letter-spacing: 6px; line-height: 1;
    color: var(--ink); text-transform: uppercase;
  }
  .brand-sub {
    font-weight: 500; font-size: 28px; letter-spacing: 7px; line-height: 1;
    color: var(--ink); text-transform: uppercase;
  }
  .brand-tag {
    font-family: "Alegreya Sans", sans-serif; font-size: 12px; letter-spacing: 1.5px;
    line-height: 1.2; color: var(--ink-soft); margin-top: 4px;
  }
  .experience {
    position: absolute; left: 440px; top: 230px;
    display: flex; align-items: flex-start; gap: 10px;
  }
  .experience-figure { color: var(--accent); font-size: 46px; line-height: 1; }
  .experience-text { font-size: 19px; line-height: 1.45; padding-top: 4px; }
  .rule { position: absolute; height: 0; border-top: 1px dashed var(--rule); }
  .rule-top { left: 440px; top: 320px; width: 360px; }
  .rule-mid { left: 440px; top: 650px; width: 360px; }
  .expertise { position: absolute; left: 440px; top: 340px; width: 370px; }
  .section-title {
    font-family: "Alegreya Sans", sans-serif; font-weight: 300;
    text-transform: uppercase; color: var(--ink); white-space: nowrap;
  }
  .expertise .section-title { font-size: 28px; line-height: 1.2; margin-bottom: 8px; }
  .expertise-list {
    list-style: none; font-size: 18px; line-height: 1.4; color: var(--ink-soft); white-space: nowrap;
  }
  .services { position: absolute; left: 40px; top: 680px; width: 760px; }
  .services .section-title { font-size: 44px; line-height: 1.1; margin-bottom: 20px; }
  .services-grid {
    list-style: none;
    display: grid;
    grid-template-columns: 200px 250px 250px;
    grid-template-rows: repeat(6, 46px);
    column-gap: 24px; row-gap: 12px;
  }
  .service {
    display: flex; align-items: center; gap: 10px;
    font-size: 16px; line-height: 1.1; color: var(--ink-soft); white-space: nowrap;
  }
  .service svg { flex: none; width: 30px; height: 36px; }
  .c1 { grid-column: 1; } .c2 { grid-column: 2; } .c3 { grid-column: 3; }
  .r1 { grid-row: 1; } .r2 { grid-row: 2; } .r3 { grid-row: 3; }
  .r4 { grid-row: 4; } .r5 { grid-row: 5; } .r6 { grid-row: 6; }
  .service-wide { grid-column: 1 / span 2; }
</style>
</head>
<body>
  <main class="flyer">
    <div class="top-band"></div>
    <div class="hero-image" role="img" aria-label="Black padlock with open shackle on dark background"></div>

    <div class="brand">
      <span class="brand-mark"></span>
      <div class="brand-text">
        <span class="brand-name">Valdren</span>
        <span class="brand-sub">Services</span>
        <span class="brand-tag">a Security Management Company</span>
      </div>
    </div>

    <div class="experience">
      <span class="experience-figure">25+</span>
      <p class="experience-text">Years of experience in Security<br>and Law Enforcement</p>
    </div>

    <div class="rule rule-top"></div>

    <section class="expertise">
      <h2 class="section-title">Areas of Expertise</h2>
      <ul class="expertise-list">
        <li>Security Management</li>
        <li>Security Department Reorganization</li>
        <li>Physical Security</li>
        <li>Electronic Security</li>
        <li>Information Security</li>
        <li>Transportation Security</li>
        <li>Security in Highly Regulated environments</li>
      </ul>
    </section>

    <div class="rule rule-mid"></div>

    <section class="services">
      <h2 class="section-title">Services Offered</h2>
      <svg width="0" height="0" style="position:absolute">
        <defs>
          <symbol id="shield" viewBox="0 0 34 40">
            <path d="M3 4 L31 4 L31 20 C31 30 24 35 17 38 C10 35 3 30 3 20 Z" fill="var(--shield)"/>
          </symbol>
        </defs>
      </svg>
      <ul class="services-grid">
        <li class="service c1 r1"><svg><use href="#shield"/></svg>Security<br>Management</li>
        <li class="service c1 r2"><svg><use href="#shield"/></svg>Security Risk<br>Management</li>
        <li class="service c1 r3"><svg><use href="#shield"/></svg>Threat<br>Assessments</li>
        <li class="service c1 r4"><svg><use href="#shield"/></svg>RFP/RFQ</li>
        <li class="service c1 r5"><svg><use href="#shield"/></svg>Security Program<br>Review</li>
        <li class="service service-wide r6"><svg><use href="#shield"/></svg>Litigation Planning and Consulting</li>
        <li class="service c2 r1"><svg><use href="#shield"/></svg>Security Management<br>Mentoring/Development</li>
        <li class="service c2 r2"><svg><use href="#shield"/></svg>Security Performance<br>Testing (Red Team)</li>
        <li class="service c2 r3"><svg><use href="#shield"/></svg>Vulnerability<br>Assessments</li>
        <li class="service c2 r4"><svg><use href="#shield"/></svg>Security Policy<br>Development</li>
        <li class="service c2 r5"><svg><use href="#shield"/></svg>Security System Design<br>Management</li>
        <li class="service c3 r1"><svg><use href="#shield"/></svg>Risk Assessments</li>
        <li class="service c3 r2"><svg><use href="#shield"/></svg>Security Audits</li>
        <li class="service c3 r3"><svg><use href="#shield"/></svg>Security Planning</li>
        <li class="service c3 r4"><svg><use href="#shield"/></svg>Project management</li>
        <li class="service c3 r5"><svg><use href="#shield"/></svg>High Risk Planning</li>
      </ul>
    </section>
  </main>
</body>
</html>
```